Sophrologist needs a cool signage at door entrance

I need signage for dr in sophrology based in Belgium (french speaking). The signed should capture the name the "Mireille Vantoorn" - "Naturopathe-Sophrologue-Reiki" and a catchphrase = (Healthy way of life)
« Fais du bien à ton corps, pour que ton âme ait envie d’y rester »
Requirements
Must have
- Hey,
Thats the instagram account for some inspiration www.instagram.com/mireille_serene_wellbeing
Light colors, green, blue
Healthy way of life
Size is 45cm wide on 30 cm high
The signage will be placed in front off woof pannel

```html
<!DOCTYPE html>
<html lang="fr">
<head>
<meta charset="utf-8">
<title>Mireille Vantoorn – Naturopathe-Sophrologue-Reiki</title>
<link href="https://fonts.googleapis.com/css2?family=Noto+Serif:wght@400;700&family=Sacramento&display=swap" rel="stylesheet">
<style>
  :root {
    --backdrop: #22231e;
    --sign-white: #ffffff;
    --name-green: #0b5e45;
    --title-plum: #5a2a5e;
    --script-ink: #2b2b2b;
    --wave-violet: #8e3a9a;
    --wave-blue: #2f4fa0;
    --wave-teal: #1f8f8a;
    --wave-green: #2aa56a;
    --wave-coral: #f28c78;
    --wave-yellow: #f1e63a;
    --wave-sky: #5cc3ee;
  }
  html, body {
    margin: 0;
    padding: 0;
    width: 975px;
    height: 1200px;
    overflow: hidden;
    background: var(--backdrop);
  }
  .sign {
    position: absolute;
    left: 0;
    top: 275px;
    width: 975px;
    height: 650px;
    background: var(--sign-white);
    overflow: hidden;
  }
  .sign__decor {
    position: absolute;
    inset: 0;
    width: 975px;
    height: 650px;
  }
  .sign__name {
    position: absolute;
    left: 0;
    right: 0;
    top: 160px;
    margin: 0;
    text-align: center;
    font-family: "Noto Serif", Georgia, serif;
    font-weight: 700;
    font-size: 70px;
    line-height: 1;
    letter-spacing: 2px;
    color: var(--name-green);
  }
  .sign__profession {
    position: absolute;
    left: 0;
    right: 0;
    top: 258px;
    margin: 0;
    text-align: center;
    font-family: "Noto Serif", Georgia, serif;
    font-weight: 400;
    font-size: 34px;
    line-height: 1;
    color: var(--title-plum);
  }
  .sign__motto {
    position: absolute;
    left: 0;
    right: 0;
    top: 364px;
    margin: 0;
    text-align: center;
    font-family: "Sacramento", cursive;
    font-size: 50px;
    line-height: 44px;
    color: var(--script-ink);
  }
</style>
</head>
<body>
  <main class="sign">
    <svg class="sign__decor" viewBox="0 0 975 650">
      <defs>
        <linearGradient id="top-tones" x1="0" y1="0" x2="1" y2="0">
          <stop offset="0" stop-color="var(--wave-blue)"/>
          <stop offset="0.3" stop-color="var(--wave-violet)"/>
          <stop offset="0.65" stop-color="var(--wave-blue)"/>
          <stop offset="1" stop-color="var(--wave-green)"/>
        </linearGradient>
        <linearGradient id="bottom-tones" x1="0" y1="0" x2="1" y2="0">
          <stop offset="0" stop-color="var(--wave-coral)"/>
          <stop offset="0.22" stop-color="var(--wave-yellow)"/>
          <stop offset="0.42" stop-color="var(--wave-sky)"/>
          <stop offset="0.65" stop-color="var(--wave-violet)"/>
          <stop offset="0.85" stop-color="var(--wave-blue)"/>
          <stop offset="1" stop-color="var(--wave-teal)"/>
        </linearGradient>
        <linearGradient id="fade-down" x1="0" y1="0" x2="0" y2="1">
          <stop offset="0" stop-color="#fff" stop-opacity="0.55"/>
          <stop offset="1" stop-color="#fff" stop-opacity="0"/>
        </linearGradient>
        <linearGradient id="fade-up" x1="0" y1="1" x2="0" y2="0">
          <stop offset="0" stop-color="#fff" stop-opacity="0.55"/>
          <stop offset="1" stop-color="#fff" stop-opacity="0"/>
        </linearGradient>
        <mask id="top-mask"><rect x="0" y="0" width="975" height="120" fill="url(#fade-down)"/></mask>
        <mask id="bottom-mask"><rect x="0" y="500" width="975" height="150" fill="url(#fade-up)"/></mask>
      </defs>
      <rect role="img" aria-label="Decorative band of flowing line waves in blue, violet and green along the top edge" x="0" y="0" width="975" height="120" fill="url(#top-tones)" mask="url(#top-mask)"/>
      <rect role="img" aria-label="Decorative band of flowing line waves in coral, yellow, sky blue, violet and teal along the bottom edge" x="0" y="500" width="975" height="150" fill="url(#bottom-tones)" mask="url(#bottom-mask)"/>
    </svg>
    <h1 class="sign__name">Mireille Vantoorn</h1>
    <p class="sign__profession">Naturopathe-Sophrologue-Reiki</p>
    <p class="sign__motto">Fais du bien a ton corps,<br>pour que ton ame ait envie d'y rester</p>
  </main>
</body>
</html>
```